Billboard design - consider what a billboard is

Design a billboard using my logo - Billboard is 6m x 3m
A Billboard is advertising for my company that is on a big sign.

Has to be clean and easy to read, and ideally highlights that we are Residential and Commercial builders.

Keep it clean and easy to read

The contact number for the board is

027 584 9071
www.fernridgebuildworks.co.nz
info@fernridgebuildworks.co.nz

Doesnt have to have all contact details if it doesnt fit

Has to catch peoples attention to contact us if they need a builder

Can you please change the sign to be all white writing, with black background ?
Updates

Please consider what a billboard is...

The design needs to be suitable for a billboard..

Target Market(s)

people driving past

Industry/Entity Type

Construction

Logo Text

Wellington Builder, website email address, contact number

Colors
0054AA
0677BA
7BADD7
CADEEF
E8F1F8

Requirements
Must have
• Easy to read
Nice to have
• easy to read, can clearly see contact details

```html
<!DOCTYPE html>
<html lang="en">
<head>
<meta charset="utf-8">
<title>Fernridge Buildworks Billboard</title>
<link href="https://fonts.googleapis.com/css2?family=Montserrat:wght@300;700;800&display=swap" rel="stylesheet">
<style>
  :root {
    --page: #e9ecef;
    --board: #ffffff;
    --brown: #6d6361;
    --blue: #5b8ccc;
    --white: #ffffff;
  }
  * { margin: 0; padding: 0; box-sizing: border-box; }
  html, body { width: 1200px; height: 730px; overflow: hidden; background: var(--page); }
  body { font-family: "Montserrat", sans-serif; }
  .billboard {
    position: absolute; left: 0; top: 65px;
    width: 1200px; height: 600px;
    background: var(--board); overflow: hidden;
  }
  .headline-bar {
    position: absolute; left: 22px; top: 190px;
    width: 9px; height: 190px; background: var(--blue);
  }
  .headline {
    position: absolute; left: 48px; top: 182px;
    font-weight: 800; font-size: 56px; line-height: 64px;
    color: var(--brown); letter-spacing: 1px;
  }
  .headline .amp { color: var(--blue); }
  .brand {
    position: absolute; left: 640px; top: 120px;
    display: flex; align-items: center; gap: 26px;
  }
  .brand-square { width: 60px; height: 60px; background: var(--blue); flex: none; }
  .brand-name {
    font-weight: 800; font-size: 76px; line-height: 82px;
    color: var(--blue);
  }
  .contact-bands { position: absolute; left: 0; top: 0; }
  .contact-label {
    position: absolute; left: 26px; top: 445px; height: 65px;
    display: flex; align-items: center;
    font-weight: 300; font-size: 36px; line-height: 1; color: var(--white);
  }
  .contact-line {
    position: absolute; display: flex; align-items: center; gap: 14px;
    color: var(--white); font-weight: 700; line-height: 1;
  }
  .contact-email { left: 420px; top: 435px; height: 75px; font-size: 30px; }
  .contact-phone { left: 24px; top: 525px; height: 75px; font-size: 50px; font-weight: 800; }
  .contact-web { left: 570px; top: 520px; height: 80px; font-size: 28px; }
  .contact-line svg { flex: none; }
</style>
</head>
<body>
<main class="billboard">
  <div class="headline-bar"></div>
  <h1 class="headline">RESIDENTIAL <span class="amp">&amp;</span><br>COMMERCIAL<br>BUILDERS.</h1>

  <div class="brand">
    <div class="brand-square"></div>
    <div class="brand-name">Fernridge<br>Buildworks</div>
  </div>

  <svg class="contact-bands" width="1200" height="600" viewBox="0 0 1200 600" aria-hidden="true">
    <polygon points="0,445 345,445 385,510 0,510" fill="var(--brown)"/>
    <polygon points="370,435 1200,435 1200,510 410,510" fill="var(--blue)"/>
    <polygon points="0,525 520,525 470,600 0,600" fill="var(--blue)"/>
    <polygon points="545,520 1200,520 1200,600 495,600" fill="var(--brown)"/>
  </svg>

  <div class="contact-label">CONTACT US:</div>

  <div class="contact-line contact-email">
    <svg width="40" height="30" viewBox="0 0 40 30" fill="none" stroke="#fff" stroke-width="2.5">
      <rect x="2" y="2" width="36" height="26"/><path d="M2 2 L20 17 L38 2 M2 28 L15 13 M38 28 L25 13"/>
    </svg>
    <span>info@fernridgebuildworks.co.nz</span>
  </div>

  <div class="contact-line contact-phone">
    <svg width="34" height="40" viewBox="0 0 34 40" fill="#fff">
      <path d="M9 4 L15 12 L11 17 Q14 25 20 29 L25 25 L32 32 L27 38 Q12 36 4 18 Q3 9 9 4 Z"/>
    </svg>
    <span>027 584 9071</span>
  </div>

  <div class="contact-line contact-web">
    <svg width="36" height="36" viewBox="0 0 36 36" fill="none" stroke="#fff" stroke-width="2.2">
      <circle cx="18" cy="18" r="15"/><ellipse cx="18" cy="18" rx="7" ry="15"/>
      <path d="M3 18 H33 M6 10 H30 M6 26 H30 M18 3 V33"/>
    </svg>
    <span>www.fernridgebuildworks.co.nz</span>
  </div>
</main>
</body>
</html>
```